Luxury Wine Label for New Startup Winery

We need a wine label for our new winery startup. We have worked with a local designer but do not feel the resulting label / logo have the elevation required to present our brand as a luxury wine. Our winery is called "Harrowgate Vineyards" and we are focused on extremely high quality hand crafted artisan and estate wines from the Pacific Northwest.
We would like to see designs that utilize a tree line, or other imagery that represents the "Harrowgate" part of our company name. Another interesting feature could be wood grain.
A logo will be required based on your design so please design with this in mind:
This logo should be consistent with the wine bottle label design, and should be representative of our high end exclusive wine while giving a sense of place (Oregon/ Pacific Northwest.)
I will supply an image of the design we received from our local designer, PLEASE NOTE: in general we do like wood grain and tree line concepts but feel the execution was poorly done.
ATTN: Logo design should be suitable for use on: Bottles (Red wine/rose/white wine), Bussiness cards, vehicle signage, business signage, etc
P.S.:
If you have a design that is not outside the box we are still interested in seeing it.
Label is for a burgundy style bottle with a label height of 3.5 - 4" and a width of 3.5-4"
any label <= 4"x4" and >=3.5"x3.5" will be acceptable:
HOWEVER Width should be greater than or equal to height due to the bottle format
Target Market(s)
Wine enthusiasts with adequate discretionary budgets to afford $100 bottles of wine.
Industry/Entity Type
Wine / Winery
Requirements
Must have
- A sense of luxury, a feel of exclusivity, and a theme consistent with our product and brand name
Nice to have
- Tree line, wood grain or other wood themes. Serif fonts
Should not have
- anything cheesy, off topic, hard to read script fonts or anything that makes the label hard to read from a few feet away or too busy

```html
<!DOCTYPE html>
<html lang="en">
<head>
<meta charset="utf-8">
<title>Harrowgate Vineyards — Wine Label</title>
<link rel="stylesheet" href="https://fonts.googleapis.com/css2?family=Antonio:wght@300&family=Mr+Dafoe&family=Oswald:wght@300&display=swap">
<style>
  :root {
    --page: #efefef;
    --label-black: #0d0d0e;
    --label-charcoal: #2a2a2c;
    --label-smoke: #4a4a4e;
    --gold: #c9a24a;
    --gold-light: #e6c877;
    --gold-deep: #8e6a26;
    --copper: #b8874f;
  }
  html, body {
    margin: 0;
    width: 1139px;
    height: 1200px;
    overflow: hidden;
    background: var(--page);
  }
  .canvas {
    position: relative;
    width: 1139px;
    height: 1200px;
  }
  .label {
    position: absolute;
    left: 70px;
    top: 150px;
    width: 1000px;
    height: 900px;
  }
  .label-art {
    position: absolute;
    inset: 0;
    width: 1000px;
    height: 900px;
  }
  .brand-name {
    position: absolute;
    left: 0;
    right: 0;
    top: 130px;
    margin: 0;
    text-align: center;
    font-family: "Antonio", "Oswald", sans-serif;
    font-weight: 300;
    font-size: 84px;
    letter-spacing: 6px;
    text-transform: uppercase;
    color: var(--gold);
  }
  .tagline {
    position: absolute;
    left: 0;
    right: 0;
    top: 640px;
    margin: 0;
    text-align: center;
    font-family: "Mr Dafoe", cursive;
    font-size: 46px;
    line-height: 1.25;
    color: var(--gold);
  }
  .volume {
    position: absolute;
    left: 0;
    right: 0;
    top: 790px;
    margin: 0;
    text-align: center;
    font-family: "Oswald", sans-serif;
    font-weight: 300;
    font-size: 26px;
    letter-spacing: 2px;
    color: var(--gold-deep);
  }
</style>
</head>
<body>
<main class="canvas">
  <section class="label">
    <svg class="label-art" viewBox="0 0 1000 900" xmlns="http://www.w3.org/2000/svg">
      <defs>
        <linearGradient id="stone" x1="0" y1="0" x2="0.3" y2="1">
          <stop offset="0" stop-color="var(--label-charcoal)"/>
          <stop offset="0.35" stop-color="var(--label-black)"/>
          <stop offset="0.7" stop-color="var(--label-charcoal)"/>
          <stop offset="1" stop-color="var(--label-smoke)"/>
        </linearGradient>
        <radialGradient id="estate" cx="0.5" cy="0.55" r="0.55">
          <stop offset="0" stop-color="var(--gold-light)"/>
          <stop offset="0.45" stop-color="var(--gold)"/>
          <stop offset="0.8" stop-color="#3a2d12"/>
          <stop offset="1" stop-color="var(--label-black)"/>
        </radialGradient>
      </defs>

      <path class="label-ground" role="img" aria-label="Marbled black and grey agate pattern"
            d="M0 40 Q250 0 500 30 T1000 20 L1000 870 Q750 900 500 870 T0 880 Z"
            fill="url(#stone)"/>

      <g class="gold-lines" fill="none" stroke="var(--copper)" stroke-width="4">
        <path d="M0 40 Q250 0 500 30 T1000 20"/>
        <path d="M0 110 Q200 60 420 90 Q650 130 1000 70" stroke-width="3"/>
        <path d="M0 520 Q120 460 260 470" stroke-width="3"/>
        <path d="M740 470 Q880 470 1000 540" stroke-width="3"/>
        <path d="M0 600 Q300 560 520 610 Q760 660 1000 620" stroke-width="2" opacity="0.6"/>
        <path d="M0 880 Q250 840 500 870 T1000 870"/>
      </g>

      <ellipse cx="500" cy="440" rx="265" ry="180" fill="var(--label-black)" stroke="var(--copper)" stroke-width="5"/>
      <ellipse class="estate-scene" role="img" aria-label="Engraved vineyard estate: chateau towers, rows of vines, trees and grape clusters"
               cx="500" cy="445" rx="215" ry="130" fill="url(#estate)"/>
    </svg>

    <h1 class="brand-name">Harrowgate Vineyards</h1>
    <p class="tagline">Premium Quality Hand Crafted<br>Artisan and Estate Wines from the Pacific Northwest</p>
    <p class="volume">700ML | 12.5 % ALCOHOL</p>
  </section>
</main>
</body>
</html>
```